QRV (Guaranteed Project)

**Note: The girl image is not mandatory, that was just an idea, it may even look better with just text and no girl

TEXT (Lorne Bexley and Vantro logos large please):

PEOPLE GET READY (the font from the image below for people get ready looks good, kind of retro)

QRV WEEKEND 2014
SUNDAY MAY 25

430-9pm

QRV after party starts at 9pm-2am

Featuring
LORNE BEXLEY (SF) (use logo, largest name)
VANTRO (Sac) (use logo w/out the text below it, and slightly smaller than lorne bexley)

at K@Z Uptown 2847 J Street 21+

Project Deadline Extended
Reason: The mgr wants to review them and hasn't said yes yet.

Target Market(s)

House/Electronic Music Night Club

Font styles to use
Sans Serif

Colors
ec2027
ffffff

Requirements
Nice to have
• Would look nice with the red background and maybe a reddish filter on the girl

```html
<!DOCTYPE html>
<html lang="en">
<head>
<meta charset="utf-8">
<title>People Get Ready – QRV Weekend 2014</title>
<link rel="stylesheet" href="https://fonts.googleapis.com/css2?family=Orbitron:wght@500;700;900&display=swap">
<style>
  :root {
    --red: #ec2027;
    --red-deep: #8a0a10;
    --red-dark: #3a0306;
    --ink: #120102;
    --white: #ffffff;
    --paper: #f7f7f5;
  }
  * { margin: 0; padding: 0; box-sizing: border-box; }
  html, body {
    width: 800px; height: 1200px; overflow: hidden;
    background: var(--paper);
  }
  .poster {
    position: relative;
    width: 800px; height: 1200px;
    background: var(--paper);
    padding: 22px 24px;
    font-family: "Orbitron", sans-serif;
    color: var(--white);
  }
  .artwork {
    position: relative;
    width: 100%; height: 100%;
    overflow: hidden;
    background: linear-gradient(180deg, var(--red-deep) 0%, var(--red-dark) 70%, var(--ink) 100%);
  }
  .hero-photo {
    position: absolute; left: 0; top: 0;
    width: 100%; height: 760px;
    background:
      radial-gradient(ellipse 38% 42% at 50% 38%, #e9b7a8 0%, #c9706a 45%, rgba(200,40,40,0) 75%),
      radial-gradient(ellipse 80% 70% at 50% 40%, var(--red) 0%, var(--red-deep) 60%, var(--red-dark) 100%);
  }
  .hero-photo::after {
    content: ""; position: absolute; left: 0; right: 0; bottom: 0; height: 260px;
    background: linear-gradient(180deg, rgba(58,3,6,0) 0%, var(--red-dark) 100%);
  }
  .headline {
    position: absolute; left: 0; top: 610px;
    width: 100%; height: 200px;
  }
  .headline text {
    font-family: "Orbitron", sans-serif;
    font-weight: 900;
    fill: var(--white);
  }
  .details {
    position: absolute; left: 0; right: 0; top: 808px;
    text-align: center;
    font-weight: 700;
    text-transform: uppercase;
    letter-spacing: 1px;
  }
  .rule {
    width: 560px; height: 1px; margin: 0 auto;
    background: rgba(255,255,255,0.55);
  }
  .event-date { font-size: 19px; line-height: 22px; margin-top: 10px; }
  .event-time { font-size: 19px; line-height: 22px; margin-top: 12px; }
  .after-party { font-size: 19px; line-height: 22px; margin-bottom: 10px; }
  .featuring { font-size: 17px; margin-top: 12px; letter-spacing: 2px; }
  .lineup {
    display: flex; justify-content: center; align-items: center;
    gap: 40px; margin-top: 24px; height: 70px;
    text-transform: none;
  }
  .act { display: flex; align-items: center; gap: 12px; font-weight: 700; color: var(--white); letter-spacing: 0; }
  .act-mark { background: var(--white); flex: none; }
  .act--headliner { font-size: 34px; }
  .act--headliner .act-mark { width: 58px; height: 58px; border-radius: 50%; }
  .act--support { font-size: 28px; }
  .act--support .act-mark { width: 26px; height: 26px; }
  .partner-badge { width: 34px; height: 40px; background: var(--white); flex: none; }
  .venue { font-size: 19px; line-height: 23px; margin-top: 34px; }
</style>
</head>
<body>
  <main class="poster">
    <div class="artwork">
      <div class="hero-photo" role="img" aria-label="Photo of a woman framing her face with her hands, bathed in red light streaks and white sparkles"></div>

      <svg class="headline" viewBox="0 0 752 200" aria-label="People Get Ready">
        <text x="376" y="106" text-anchor="middle" font-size="92" textLength="676" lengthAdjust="spacingAndGlyphs">PEOPLE</text>
        <text x="376" y="190" text-anchor="middle" font-size="78" textLength="676" lengthAdjust="spacingAndGlyphs">GET READY</text>
      </svg>

      <section class="details">
        <div class="rule"></div>
        <p class="event-date">QRV Weekend 2014<br>Sunday May 25</p>
        <p class="event-time">430-9pm</p>
        <p class="after-party">QRV after party starts at 9pm-2am</p>
        <div class="rule"></div>
        <p class="featuring">Featuring</p>
        <div class="lineup">
          <div class="act act--headliner"><span class="act-mark"></span>lorne bexley</div>
          <div class="act act--support"><span class="act-mark"></span>VANTRO</div>
          <span class="partner-badge" role="img" aria-label="Partner badge"></span>
        </div>
        <p class="venue">House music at it's finest<br>at K@Z Uptown 2847 J Street 21+</p>
      </section>
    </div>
  </main>
</body>
</html>
```